Design a helpdesk ticketing platform *

We are launching a helpdesk ticketing platform. Very much like lumidesk.example, brightowl.example, calmhub.example, tidyqueue.example etc. We have a full mid-fidelity prototype built and we want someone to build the full fidelity of the product.

You can view the full mid-fidelity prototype here: https://shortlink.example/Qw8pLk

The best way moving forward is to just design the following 4 pages

- Main Dashboard https://shortlink.example/48vRxN
- All tickets https://shortlink.example/jbdYsW
- Viewing a ticket https://shortlink.example/mHqLtB
- Contacts https://shortlink.example/yKeoPd

Target Market(s)

Small business owners

Industry/Entity Type

Saas

Number of Pages Required

4 page

Font styles to use
Serif
Sans Serif

Colors

Designer to choose colors to be used in the design.

Requirements
Must have
• Must follow the prototype exactly. We are not looking for any UX changes. We want the designe xactly as the prototype is. We are only looking for design ideas.
Should not have
• modern, clean. We'd love to see the primary color as yellow, purple, orange, green or blue. You choose which one you think looks best and go with that.

```html
<!DOCTYPE html>
<html lang="en">
<head>
<meta charset="utf-8">
<title>ticketnest – ticket view</title>
<link rel="stylesheet" href="https://fonts.googleapis.com/css2?family=Poppins:wght@300;400;500;600&display=swap">
<style>
:root{
  --bg:#f5f5f5;
  --primary:#4a74e8;
  --primary-dark:#3f66d6;
  --green:#62d99a;
  --side:#333d4e;
  --side-dark:#2b3442;
  --side-text:#c9d0dc;
  --side-muted:#9aa4b4;
  --panel:#f4f6f9;
  --white:#ffffff;
  --line:#e3e7ee;
  --text:#333a46;
  --muted:#8a93a2;
  --faint:#b7bec9;
  --avatar:#c89a7a;
}
*{box-sizing:border-box;margin:0;padding:0}
html,body{width:982px;height:1200px;overflow:hidden;background:var(--bg);font-family:"Poppins",sans-serif;color:var(--text)}
.wordmark{position:absolute;top:88px;left:0;width:982px;text-align:center;font-size:50px;font-weight:400;color:var(--primary);letter-spacing:0.5px}
.app{position:absolute;top:200px;left:41px;width:900px;height:640px;background:var(--panel);display:grid;grid-template-columns:166px 1fr;grid-template-rows:48px 1fr;box-shadow:0 20px 50px rgba(40,50,70,.08)}
.brand{background:var(--primary);color:#fff;display:flex;align-items:center;justify-content:space-between;padding:0 14px;font-size:15px;font-weight:600}
.burger{width:14px;height:10px;border-top:2px solid #fff;border-bottom:2px solid #fff;position:relative}
.burger::after{content:"";position:absolute;left:0;right:0;top:2px;border-top:2px solid #fff}
.topbar{background:var(--white);display:flex;align-items:center;border-bottom:1px solid var(--line)}
.crumbs{width:158px;padding-left:14px;font-size:8px;color:var(--faint);border-right:1px solid var(--line);height:100%;display:flex;align-items:center;gap:6px}
.crumbs b{color:var(--text);font-weight:500}
.search{flex:1;padding-left:16px;font-size:8px;color:var(--faint);display:flex;align-items:center;gap:6px}
.user{width:158px;height:100%;border-left:1px solid var(--line);display:flex;align-items:center;padding:0 12px;gap:8px;font-size:8px}
.user .dots{margin-left:auto;color:var(--muted)}
.logout{width:48px;height:100%;background:var(--primary);display:flex;align-items:center;justify-content:center}
.avatar{width:22px;height:22px;border-radius:50%;background:radial-gradient(circle at 50% 40%,#e2bd9f,var(--avatar));flex:none}
.sidebar{background:var(--side);padding-top:14px;position:relative}
.new-ticket{margin:0 14px 22px;height:22px;background:var(--green);color:#fff;font-size:7px;font-weight:500;letter-spacing:.5px;display:flex;align-items:center;justify-content:space-between;padding:0 10px 0 18px}
.nav-item{height:25px;display:flex;align-items:center;gap:9px;padding-left:16px;font-size:7.5px;font-weight:500;letter-spacing:.6px;color:var(--side-text);text-transform:uppercase}
.nav-item.active{background:var(--side-dark);color:#fff;border-left:2px solid var(--primary);padding-left:14px}
.nav-item.dash{background:var(--side-dark);color:#fff}
.nav-item .caret{margin-left:auto;margin-right:14px;font-size:6px}
.subnav{margin:8px 0 12px 22px;border-left:1px solid #485366;padding-left:14px}
.subnav li{list-style:none;font-size:7px;letter-spacing:.4px;color:var(--side-muted);height:15px;text-transform:uppercase}
.subnav li.current{color:var(--primary)}
.subnav .gap{height:10px}
.ico{width:8px;height:8px;background:var(--side-text);border-radius:2px;opacity:.8}
.footer{position:absolute;bottom:14px;left:14px;font-size:8px;color:var(--side-text);line-height:1.4}
.body{display:grid;grid-template-columns:1fr 158px}
.main{border-right:1px solid var(--line);overflow:hidden}
.actions{height:50px;display:flex;align-items:center;gap:6px;padding:0 14px;border-bottom:1px solid var(--line)}
.btn{height:20px;padding:0 10px;border:1px solid #cfd5df;border-radius:10px;font-size:7.5px;color:var(--muted);display:flex;align-items:center;gap:4px;background:var(--white)}
.btn.primary{background:var(--primary);border-color:var(--primary);color:#fff}
.pager{margin-left:auto;color:var(--faint);font-size:10px;letter-spacing:8px}
.show-act{height:20px;padding:0 12px;background:#b4bcc8;color:#fff;font-size:7.5px;display:flex;align-items:center}
.ticket{padding:16px 14px 0}
.ticket-head{display:flex;justify-content:space-between;align-items:baseline}
.ticket-head h1{font-size:13px;font-weight:500}
.date{font-size:6.5px;color:var(--faint);letter-spacing:.3px}
.requester{display:flex;gap:10px;margin:14px 0 22px 10px}
.requester .name{font-size:9px}
.requester .name span{color:var(--faint)}
.tags{display:flex;gap:6px;align-items:center;font-size:7px;color:var(--muted);margin-top:6px}
.tag{font-size:5.5px;padding:2px 5px;background:var(--white);border:1px solid var(--line);color:var(--text);letter-spacing:.3px}
.msg{background:var(--white);border-top:1px solid var(--line);display:grid;grid-template-columns:26px 1fr auto 14px;gap:10px;align-items:center;padding:12px 12px;margin-bottom:1px}
.msg .who{font-size:7.5px;font-weight:500}
.msg .snippet{font-size:7.5px;color:var(--muted);margin-top:2px}
.msg .when{font-size:6.5px;color:var(--muted)}
.msg .more{font-size:8px;color:var(--faint);text-align:center}
.msg.open{align-items:start}
.msg.open .body-text{font-size:7.5px;color:var(--muted);line-height:1.5;margin-top:14px}
.props{padding:0}
.props h2{font-size:9px;font-weight:500;height:50px;display:flex;align-items:center;padding-left:14px;border-bottom:1px solid var(--line)}
.field{padding:0 14px;margin-top:10px}
.field label{display:block;font-size:7.5px;margin-bottom:5px}
.select{height:20px;border:1px solid #dde2ea;background:var(--white);font-size:7.5px;color:var(--faint);display:flex;align-items:center;justify-content:space-between;padding:0 8px}
.update{margin:16px 14px 0;height:20px;background:var(--green);color:#fff;font-size:7px;letter-spacing:.5px;display:flex;align-items:center;justify-content:center}
.info{width:48px;position:absolute;top:48px;right:0;height:50px;display:flex;align-items:center;justify-content:center;font-size:10px;font-style:italic;color:var(--muted)}
</style>
</head>
<body>
<div class="wordmark">ticketnest</div>

<div class="app">
  <div class="brand">ticketnest<span class="burger"></span></div>
  <div class="topbar">
    <div class="crumbs">Tickets › All Tickets › <b>#10</b></div>
    <div class="search">
      <svg width="9" height="9" viewBox="0 0 10 10"><circle cx="4" cy="4" r="3" fill="none" stroke="#b7bec9" stroke-width="1.2"/><path d="M6.5 6.5L9 9" stroke="#b7bec9" stroke-width="1.2"/></svg>
      Search here …
    </div>
    <div class="user"><span class="avatar" role="img" aria-label="Agent profile photo"></span>Marcus Ellery<span class="dots">⋮</span></div>
    <div class="logout"><svg width="12" height="12" viewBox="0 0 12 12"><path d="M5 1H1v10h4M5 6h6M8.5 3.5L11 6 8.5 8.5" fill="none" stroke="#fff" stroke-width="1.3"/></svg></div>
  </div>

  <nav class="sidebar">
    <div class="new-ticket">NEW TICKET<span>⋮</span></div>
    <div class="nav-item dash"><span class="ico"></span>Dashboard</div>
    <div class="nav-item active"><span class="ico"></span>Tickets<span class="caret">▲</span></div>
    <ul class="subnav">
      <li class="current">All tickets</li>
      <li>My ticktets</li>
      <li>Open tickets</li>
      <li>Unassigned tickets</li>
      <li class="gap"></li>
      <li>Spam</li>
      <li>Trash</li>
    </ul>
    <div class="nav-item"><span class="ico"></span>Contacts</div>
    <div class="nav-item"><span class="ico"></span>Admin settings<span class="caret">▼</span></div>
    <div class="nav-item"><span class="ico"></span>Account &amp; billing</div>
    <div class="footer">© 2018 ticketnest.<br>All right reserved.</div>
  </nav>

  <div class="body">
    <section class="main">
      <div class="actions">
        <span class="btn">↩ Reply</span>
        <span class="btn primary">➦ Forward</span>
        <span class="btn">+ Add note</span>
        <span class="btn">⚭ Merge</span>
        <span class="btn">✕ Close</span>
        <span class="pager">‹ ›</span>
        <span class="show-act">Show Activities</span>
      </div>
      <div class="ticket">
        <div class="ticket-head"><h1>I can't reset my password</h1><span class="date">WED, 28 JAN 2018 AT 1:00 AM</span></div>
        <div class="requester">
          <span class="avatar" role="img" aria-label="Customer profile photo"></span>
          <div>
            <div class="name">Nora Whitfield <span>Ticket # 10</span></div>
            <div class="tags">Tags: <span class="tag">RESPONSE DUE ×</span><span class="tag">HELLO ×</span><span class="tag">SALES ×</span><span class="tag">+ TAGS</span></div>
          </div>
        </div>
        <div class="msg"><span class="avatar" role="img" aria-label="Customer profile photo"></span><div><div class="who">Nora Whitfield</div><div class="snippet">Hello, I am unable to reset my password for some reason. Can you ...</div></div><span class="when">JAN 2018 5:00 PM</span><span class="more">⋮</span></div>
        <div class="msg"><span class="avatar" role="img" aria-label="Agent profile photo"></span><div><div class="who">Owen Castell</div><div class="snippet">Hello Nora, The link was sent more than 12 hours ago, so it's no ...</div></div><span class="when">JAN 2018 5:00 PM</span><span class="more">⋮</span></div>
        <div class="msg"><span class="avatar" role="img" aria-label="Customer profile photo"></span><div><div class="who">Nora Whitfield</div><div class="snippet">Thanks for you help.</div></div><span class="when">JAN 2018 5:00 PM</span><span class="more">⋮</span></div>
        <div class="msg open"><span class="avatar" role="img" aria-label="Agent profile photo"></span><div><div class="who">Owen Castell</div><div class="snippet">To Nora Whitfield</div>
          <div class="body-text">Hello Nora,<br><br>If you have any additional questions or concerns please let us know.<br>Thank you for contacting CallLoom.<br><br>Kind Regards,<br>Owen</div></div><span class="when">JAN 2018 5:00 PM</span><span class="more">⋮</span></div>
      </div>
    </section>

    <aside class="props">
      <h2>Properties</h2>
      <div class="field"><label>Status</label><div class="select">Open<span>▾</span></div></div>
      <div class="field"><label>Priority</label><div class="select">Low<span>▾</span></div></div>
      <div class="field"><label>Groups</label><div class="select">Support<span>▾</span></div></div>
      <div class="field"><label>Agent</label><div class="select">Owen Castell<span>▾</span></div></div>
      <div class="field"><label>Product</label><div class="select">CallLoom<span>▾</span></div></div>
      <div class="field"><label>Miscellaneous 1</label><div class="select"></div></div>
      <div class="field"><label>Miscellaneous 2</label><div class="select"></div></div>
      <div class="update">UPDATE</div>
    </aside>
  </div>
  <div class="info">i</div>
</div>
</body>
</html>
```